Youth deer hunt give away flyer.

We need a flyer designed for a youth deer hunt giveaway that we are doing. We are an Illinois whitetail deer hunting outfitter. We house and feed our clients as well as providing them with a guided deer hunt. It needs to include images as well as details about the giveaway. Im looking for a proffesional, looking flyer

Target Market(s)

rednecks, hunters

Industry/Entity Type

Hunting

Font styles to use
Serif
Sans Serif

Colors
000000
dbdbdb
ffffff
474747

Requirements
Must have
• not sure
Nice to have
• not sure
Should not have
• not sure

```html
<!DOCTYPE html>
<html lang="en">
<head>
<meta charset="utf-8">
<title>Youth Firearm Hunt Flyer</title>
<link href="https://fonts.googleapis.com/css2?family=Cinzel:wght@400;700&family=PT+Sans:wght@400;700&display=swap" rel="stylesheet">
<style>
  :root{
    --black:#000000;
    --light:#dbdbdb;
    --white:#ffffff;
    --dark:#474747;
    --ink:#1a1a1a;
    --stage:#e9e9e9;
  }
  *{margin:0;padding:0;box-sizing:border-box}
  html,body{width:1200px;height:1200px;overflow:hidden;background:var(--stage)}
  .flyer{
    position:absolute;left:187px;top:15px;width:870px;height:1233px;
    transform:scale(0.949);transform-origin:0 0;overflow:hidden;
    background:linear-gradient(160deg,#ececec 0%,var(--light) 45%,#e6e6e6 100%);
    font-family:"PT Sans",sans-serif;color:var(--ink);
  }
  .swoosh{position:absolute;left:0;top:0}
  .brand{position:absolute;left:16px;top:158px;width:280px;text-align:center;
    font-family:"Cinzel",serif;font-weight:400;color:var(--ink);z-index:2}
  .brand-name{display:block;font-size:25px;line-height:28px;letter-spacing:.5px;white-space:nowrap}
  .brand-sub{display:block;font-size:11px;line-height:14px;letter-spacing:4px}
  .photo{position:absolute;border-radius:50%}
  .photo-trophy{left:360px;top:20px;width:316px;height:316px;border:10px solid var(--white);
    background:radial-gradient(circle at 65% 55%,#5d5f4e 0%,#2d2f25 45%,#0e0f0b 80%)}
  .photo-hunter{left:71px;top:212px;width:406px;height:406px;border:14px solid var(--white);
    background:radial-gradient(circle at 45% 55%,#7a5a36 0%,#4b3520 45%,#2a1c10 85%)}
  .photo-cabin{left:424px;top:274px;width:338px;height:338px;border:12px solid var(--black);
    background:radial-gradient(circle at 55% 45%,#c88a4e 0%,#9a5a2c 50%,#5c3418 90%)}
  .headline{position:absolute;left:240px;top:622px;width:600px;text-align:center;
    font-family:"Cinzel",serif;font-weight:700;font-size:39px;color:var(--black);letter-spacing:.5px}
  .date{position:absolute;left:263px;top:670px;width:552px;height:54px;background:var(--dark);
    color:var(--white);font-family:"Cinzel",serif;font-weight:700;font-size:40px;
    letter-spacing:7px;text-align:center;line-height:54px}
  .about{position:absolute;left:55px;top:744px;width:772px;font-size:15px;line-height:20px;text-align:justify}
  .offer-band{position:absolute;left:190px;top:886px;width:633px;height:190px;
    background:linear-gradient(90deg,#a9a9a9,#c4c4c4 60%,#b8b8b8)}
  .offer-badge{position:absolute;left:50px;top:882px;width:204px;height:200px;border-radius:50%;
    background:radial-gradient(circle at 50% 40%,#2a2a2a,var(--black) 70%);border:4px solid var(--white);
    color:var(--white);font-family:"Cinzel",serif;text-align:center;padding-top:54px;font-size:42px;line-height:42px}
  .offer-badge b{font-weight:700}
  .offer-list{position:absolute;left:265px;top:903px;width:560px;list-style:none;font-weight:700;font-size:21px;line-height:25px}
  .offer-list li{position:relative;padding-left:18px;margin-bottom:8px}
  .offer-list li::before{content:"";position:absolute;left:0;top:10px;width:7px;height:7px;border-radius:50%;background:var(--ink)}
  .footer{position:absolute;left:0;top:1099px;width:870px;height:134px;background:var(--black);color:var(--white);font-size:20px;font-weight:700}
  .contact{position:absolute;display:flex;gap:10px;align-items:flex-start;line-height:25px}
  .contact svg{flex:none;margin-top:4px}
  .address{left:60px;top:17px}
  .phone{left:62px;top:72px}
  .email{left:403px;top:16px}
  .web{left:403px;top:44px}
  .social{position:absolute;left:755px;top:24px;width:71px;height:32px;background:var(--white);display:flex;gap:8px;padding:7px 12px}
  .social span{width:18px;height:18px;background:var(--black)}
</style>
</head>
<body>
<div class="flyer">
  <svg class="swoosh" width="870" height="1100" viewBox="0 0 870 1100" aria-hidden="true">
    <path d="M560 0 C520 40 490 80 470 120" stroke="#5a5a5a" stroke-width="60" fill="none"/>
    <path d="M0 260 C140 250 300 210 420 160" stroke="#5a5a5a" stroke-width="50" fill="none"/>
    <path d="M0 325 C160 310 320 250 440 190" stroke="#9a9a9a" stroke-width="30" fill="none"/>
    <path d="M870 0 L870 322 C760 328 620 360 520 420 C380 500 200 600 0 730 L0 400 C150 380 330 260 480 150 C600 60 720 20 870 0 Z" fill="#000"/>
    <path d="M720 0 C660 30 620 60 590 90" stroke="#9a9a9a" stroke-width="26" fill="none"/>
    <path d="M870 325 C760 330 620 362 520 422 C380 502 200 602 0 740" stroke="#fff" stroke-width="10" fill="none"/>
    <path d="M835 0 C760 50 700 100 650 150" stroke="#fff" stroke-width="10" fill="none"/>
  </svg>

  <div class="brand"><span class="brand-name">Halloway Ridge</span><span class="brand-sub">OUTFITTING</span></div>

  <div class="photo photo-trophy" role="img" aria-label="Hunter in camouflage and orange cap kneeling behind a large-antlered whitetail buck at night"></div>
  <div class="photo photo-hunter" role="img" aria-label="Hunter seated in autumn woods holding the antlers of a harvested trophy buck"></div>
  <div class="photo photo-cabin" role="img" aria-label="Interior of the wood-paneled private cabin with kitchen, dining area and glass doors"></div>

  <h1 class="headline">2018 Youth Firearm Hunt</h1>
  <div class="date">October 6-8, 2018</div>

  <p class="about">Halloway Ridge Outfitting is a family owned and operated deer hunting outfitter located in Morgan and Scott Counties in west central Illinois. We provide low pressure, trophy whitetail hunts on privately owned farms across the region. The Halloways are lifelong residents and hunters of Morgan County, with the family farm being established well over 150 years ago.<br>To go along with guiding deer and turkey hunters, we also offer a wide variety of professional hunting services that include whitetail land consulting, scouting services, CRP and food plot plantings and more.</p>

  <div class="offer-band"></div>
  <div class="offer-badge">WE<br><b>OFFER</b></div>
  <ul class="offer-list">
    <li>4 night stay in our private cabin that include meals for 2 parents and the child.</li>
    <li>Guided shotgun hunt on strictly managed properties.</li>
    <li>Ground blinds in place.</li>
    <li>Permit and license fees are the hunters responsibility.</li>
  </ul>

  <footer class="footer">
    <div class="contact address">
      <svg width="16" height="20" viewBox="0 0 16 20"><path d="M8 0a7 7 0 0 0-7 7c0 5 7 13 7 13s7-8 7-13a7 7 0 0 0-7-7zm0 10a3 3 0 1 1 0-6 3 3 0 0 1 0 6z" fill="#fff"/></svg>
      <div>Caleb Halloway,1840 Ridge Road<br>Millbrook, Illinois 62000</div>
    </div>
    <div class="contact phone">
      <svg width="14" height="18" viewBox="0 0 14 18"><path d="M3 1l3 4-2 2c1 3 3 5 5 6l2-2 3 3-2 3C6 17 1 10 1 3z" fill="none" stroke="#fff" stroke-width="1.6"/></svg>
      <div>(217)555-0148</div>
    </div>
    <div class="contact email">
      <svg width="18" height="14" viewBox="0 0 18 14"><rect x="1" y="1" width="16" height="12" fill="none" stroke="#fff" stroke-width="1.6"/><path d="M1 1l8 7 8-7" fill="none" stroke="#fff" stroke-width="1.6"/></svg>
      <div>hallowayridge@mailbox.com</div>
    </div>
    <div class="contact web">
      <svg width="18" height="18" viewBox="0 0 18 18"><circle cx="9" cy="9" r="7.5" fill="none" stroke="#fff" stroke-width="1.6"/><path d="M1.5 9h15M9 1.5c-3 3-3 12 0 15M9 1.5c3 3 3 12 0 15" fill="none" stroke="#fff" stroke-width="1.2"/></svg>
      <div>www.hallowayridgeoutfitting.com</div>
    </div>
    <div class="social" aria-label="Social media links"><span></span><span></span></div>
  </footer>
</div>
</body>
</html>
```